" Possui corretores credenciados que vendem lotes e terrenos no Vale do Paraíba. A empresa não possui escritório próprio, os corretores trabalham nos plantões de vendas das incorporadoras. "

```html
<!DOCTYPE html>
<html lang="pt-BR">
<head>
<meta charset="UTF-8">
<title>Lotevale Imóveis – Papel Timbrado</title>
<link href="https://fonts.googleapis.com/css2?family=Montserrat:wght@400;500;600&display=swap" rel="stylesheet">
<style>
  :root {
    --backdrop: #ecebe8;
    --paper: #ffffff;
    --brand-yellow: #f2b331;
    --ink: #3a3a3a;
    --ink-soft: #6b6b6b;
    --watermark: #f1f1f1;
  }
  * { margin: 0; padding: 0; box-sizing: border-box; }
  html, body {
    width: 1200px;
    height: 1200px;
    overflow: hidden;
    background: var(--backdrop);
    font-family: "Montserrat", sans-serif;
  }
  .letterhead {
    position: absolute;
    left: 240px;
    top: 96px;
    width: 720px;
    height: 1014px;
    background: var(--paper);
    box-shadow: 0 6px 18px rgba(0,0,0,0.12);
    overflow: hidden;
  }
  .brand {
    position: absolute;
    top: 34px;
    left: 0;
    right: 0;
    display: flex;
    justify-content: center;
    align-items: center;
    gap: 14px;
  }
  .brand-mark {
    width: 40px;
    height: 40px;
    background: var(--brand-yellow);
  }
  .brand-text {
    display: flex;
    flex-direction: column;
    align-items: center;
  }
  .brand-name {
    font-weight: 500;
    font-size: 32px;
    line-height: 1;
    letter-spacing: 1.5px;
    color: var(--ink);
  }
  .brand-tagline {
    margin-top: 4px;
    font-weight: 500;
    font-size: 9px;
    letter-spacing: 6px;
    padding-left: 6px;
    color: var(--brand-yellow);
  }
  .watermark {
    position: absolute;
    left: 156px;
    top: 278px;
    width: 408px;
    height: 420px;
    background: var(--watermark);
  }
  .contact-bar {
    position: absolute;
    left: 108px;
    right: 108px;
    top: 955px;
    display: flex;
    justify-content: space-between;
    align-items: flex-start;
    font-size: 10px;
    color: var(--ink-soft);
  }
  .contact-item {
    display: flex;
    align-items: flex-start;
    gap: 6px;
    line-height: 1.45;
    white-space: nowrap;
  }
  .contact-icon {
    flex: none;
    width: 13px;
    height: 13px;
  }
  .footer-band {
    position: absolute;
    left: 0;
    right: 0;
    bottom: 0;
    height: 14px;
    background: var(--brand-yellow);
  }
</style>
</head>
<body>
  <main class="letterhead">
    <header class="brand">
      <span class="brand-mark"></span>
      <div class="brand-text">
        <span class="brand-name">LOTEVALE</span>
        <span class="brand-tagline">IMÓVEIS</span>
      </div>
    </header>

    <div class="watermark" aria-hidden="true"></div>

    <footer class="contact-bar">
      <div class="contact-item">
        <svg class="contact-icon" viewBox="0 0 14 14">
          <circle cx="7" cy="7" r="7" fill="var(--brand-yellow)"/>
          <path d="M4.6 3.8l1.3-.3.7 1.7-.8.6c.4.9 1.1 1.6 2 2l.6-.8 1.7.7-.3 1.3c-3 .2-5.4-2.2-5.2-5.2z" fill="#fff"/>
        </svg>
        <span>(00) 0000-0000</span>
      </div>
      <div class="contact-item">
        <svg class="contact-icon" viewBox="0 0 14 14">
          <circle cx="7" cy="7" r="7" fill="var(--brand-yellow)"/>
          <rect x="3.5" y="4.5" width="7" height="5" fill="none" stroke="#fff" stroke-width="1"/>
          <path d="M3.5 4.5L7 7.3l3.5-2.8" fill="none" stroke="#fff" stroke-width="1"/>
        </svg>
        <span>contato@lotevale.com</span>
      </div>
      <div class="contact-item">
        <svg class="contact-icon" viewBox="0 0 14 14">
          <circle cx="7" cy="7" r="7" fill="var(--brand-yellow)"/>
        </svg>
        <span>@lotevaleimoveis</span>
      </div>
      <div class="contact-item">
        <svg class="contact-icon" viewBox="0 0 14 14">
          <circle cx="7" cy="7" r="7" fill="var(--brand-yellow)"/>
          <path d="M7 11s-2.8-3-2.8-5a2.8 2.8 0 015.6 0c0 2-2.8 5-2.8 5z" fill="#fff"/>
          <circle cx="7" cy="6" r="1" fill="var(--brand-yellow)"/>
        </svg>
        <span>Endereço aqui, nº 00<br>Cidade - UF</span>
      </div>
    </footer>

    <div class="footer-band"></div>
  </main>
</body>
</html>
```